Web design for boutique law firm

Web design for law firm; practice areas include:
-international intellectual property counseling
-general corporate (contract negotiation, licensing, distribution agreements
-see my *very* outdated website at www.pvtlegalhouse.com: here is some of the home page content:

"PVT Law Group enjoys providing proactive, business-minded, efficient legal solutions for individuals and companies that benefit from major law firm experience at reasonable rates.

Some areas of emphasis include:

Counseling individuals and companies with respect to clearing, selecting, securing, managing, commercializing, and protecting intellectual property assets around the world. This includes traditional global brand management, marketing, advertising, and enforcement work as well as litigation.
PVT Law Group also provides general counseling services for individuals and businesses, from start-up advice to sophisticated business transactions strategy, agreement negotiating, dispute resolution, and litigation.
Before founding PVT Law Group in 2008, Curtis L. Abernathy led the Trademark, Copyright, & Brand Management Group for Falkner & Ingleby's Seattle office. Curtis was also a senior associate at Silicon Valley based Hartwell, Bexley, Oduya, & Penrose."

Target Market(s)

Clients/potential clients needing tier one, international intellectual property advice with "mega" law firm experience for much less than what we were/would be charging at the "mega firms".

Industry/Entity Type

Legal

Number of Pages Required

4 page

Font styles to use
Serif
Sans Serif

Colors

Designer to choose colors to be used in the design.

Requirements
Must have
• +Improvement over everything on current site at www.pvtlegalhouse.com.
• +Pictures/bios for me and my team (four of us right now).
• +Easy to update and add/remove content.
• +Must be superior in design (look, feel, ease of use, classy and elegant, but hip, reflects international practice).
• +i have logos and color schemes (see current website) but will consider improvements.
Nice to have
• Let me know your thoughts.
Should not have
• No cheese; no overt sales pitches or marketing (since law firm).

```html
<!DOCTYPE html>
<html lang="en">
<head>
<meta charset="utf-8">
<title>PVT Law Group — Home</title>
<link rel="stylesheet" href="https://fonts.googleapis.com/css2?family=Open+Sans:wght@400;600&family=Quattrocento:wght@400;700&display=swap">
<style>
  :root{
    --orange:#e8711a;
    --orange-dark:#c2611f;
    --ink:#3a3a3a;
    --text:#5b5b5b;
    --muted:#7a7a7a;
    --black:#000;
    --white:#fff;
    --pale:#f5f6f8;
    --line:#e2e2e2;
    --arrow-grey:#5d5d5d;
    --arrow-pale:#e1e2e4;
    --logo:#5c5c5c;
    --serif:"Quattrocento", Georgia, serif;
    --sans:"Open Sans", Arial, sans-serif;
  }
  *{box-sizing:border-box;margin:0;padding:0}
  html,body{width:1093px;height:1200px;overflow:hidden;background:var(--white)}
  body{position:relative;font-family:var(--sans);color:var(--text)}
  .abs{position:absolute}

  /* team strip */
  .team{left:0;top:0;width:1093px;height:186px;background:var(--black)}
  .nav-btn{width:47px;height:43px;display:flex;align-items:center;justify-content:center}
  .nav-btn svg{width:12px;height:20px}
  .nav-btn--grey{background:var(--arrow-grey)}
  .nav-btn--pale{background:var(--arrow-pale)}
  .nav-btn--orange{background:var(--orange)}
  .member{top:0;height:129px;width:410px;display:flex}
  .member__photo{width:196px;height:129px}
  .member__info{flex:1;padding:0 18px 0 22px;font-size:11.5px;line-height:18px}
  .member__info .exp{margin-top:-6px;font-family:var(--serif);font-size:12px}
  .member__info .areas{margin-top:13px}
  .member__info .areas span{font-family:var(--serif);font-size:13px}
  .member__info .rate{margin-top:14px;display:flex;align-items:center;gap:6px}
  .member--active .member__info{background:var(--orange-dark);color:var(--white)}
  .member--idle .member__info{background:var(--white);color:#333}
  .member--idle .exp{color:var(--muted)}
  .member--idle .areas span{color:var(--orange)}
  .stars{display:flex;gap:2px}
  .stars svg{width:14px;height:13px}

  /* about */
  .section-title{left:0;width:1093px;text-align:center;font-family:var(--serif);font-weight:700;font-size:24px;color:var(--ink);letter-spacing:.3px}
  .title-rule{left:509px;width:63px;height:2px;background:var(--orange)}
  .copy{left:146px;width:800px;text-align:center;font-size:11.6px;line-height:19.2px;color:var(--text)}
  .emphasis{left:428px;top:350px;width:214px;height:36px;border:1px solid #f0a36a;color:var(--orange);font-size:12px;display:flex;align-items:center;justify-content:center}
  .dash-rule{left:166px;top:462px;width:750px;border-top:1px dashed #f0a36a}
  .read-more{left:469px;top:548px;width:142px;height:38px;background:var(--orange);border:2px solid #d45f10;color:var(--white);font-family:var(--serif);font-weight:700;font-size:12.5px;display:flex;align-items:center;justify-content:center;gap:7px}
  .read-more svg{width:18px;height:18px}

  /* testimonials */
  .clients{left:0;top:624px;width:1093px;height:433px;background:var(--pale)}
  .quote{top:736px;width:266px;height:190px;background:var(--white);border:1px solid var(--line);padding:20px 18px 0 19px;font-size:11.6px;line-height:22.4px;color:var(--text)}
  .quote__tail{position:absolute;left:35px;bottom:-9px;width:16px;height:9px}
  .client{top:949px;display:flex;align-items:center;gap:15px}
  .client__avatar{width:58px;height:58px;border-radius:50%;background:radial-gradient(circle at 50% 40%,#e3d3c4,#8e8a88)}
  .client__name{font-family:var(--serif);font-size:15px;color:var(--ink)}
  .client__rate{margin-top:5px;display:flex;align-items:center;gap:6px;font-size:10.5px;color:#444;letter-spacing:.3px}

  /* partner names */
  .partners{left:0;top:1057px;width:1093px;height:143px;background:var(--black)}
  .partner{top:1113px;font-family:var(--sans);font-weight:600;font-size:27px;color:var(--logo);transform:translateX(-50%);white-space:nowrap;display:flex;align-items:center;gap:8px}
  .partner i{display:inline-block;width:22px;height:22px;border-radius:50%;background:var(--logo)}
</style>
</head>
<body>
<svg width="0" height="0" style="position:absolute">
  <defs>
    <symbol id="star" viewBox="0 0 24 23"><path d="M12 0l3.6 7.6 8.4 1-6.2 5.8 1.6 8.3L12 18.6 4.6 22.7l1.6-8.3L0 8.6l8.4-1z"/></symbol>
    <symbol id="chev-left" viewBox="0 0 12 20"><path d="M10 1L2 10l8 9" fill="none" stroke-width="1.6"/></symbol>
    <symbol id="chev-right" viewBox="0 0 12 20"><path d="M2 1l8 9-8 9" fill="none" stroke-width="1.6"/></symbol>
  </defs>
</svg>

<!-- Team strip -->
<section class="abs team" aria-label="Our team">
  <div class="abs nav-btn nav-btn--grey" style="left:5px;top:3px"><svg stroke="#222"><use href="#chev-left"/></svg></div>
  <div class="abs nav-btn nav-btn--orange" style="left:1041px;top:3px"><svg stroke="#fff"><use href="#chev-right"/></svg></div>

  <article class="abs member member--active" style="left:118px">
    <div class="member__photo" role="img" aria-label="Portrait of attorney in dark suit, black and white" style="background:linear-gradient(160deg,#9a9a9a,#3c3c3c)"></div>
    <div class="member__info">
      <p class="exp">experience in this fieold.</p>
      <p class="areas">Practice Areas: <span>Individual and corporate identities, brands, and reputations</span></p>
      <div class="rate">Reviews:
        <div class="stars" style="fill:#fff"><svg><use href="#star"/></svg><svg><use href="#star"/></svg><svg><use href="#star"/></svg><svg><use href="#star"/></svg><svg><use href="#star"/></svg></div>
      </div>
    </div>
  </article>

  <article class="abs member member--idle" style="left:566px">
    <div class="member__photo" role="img" aria-label="Portrait of attorney in navy suit" style="background:linear-gradient(160deg,#c9cfd6,#2b3346)"></div>
    <div class="member__info">
      <p class="exp">experience in this fieold.</p>
      <p class="areas">Practice Areas: <span>Individual and corporate identities, brands, and reputations</span></p>
      <div class="rate">Reviews:
        <div class="stars" style="fill:var(--orange)"><svg><use href="#star"/></svg><svg><use href="#star"/></svg><svg><use href="#star"/></svg><svg><use href="#star"/></svg><svg><use href="#star"/></svg></div>
      </div>
    </div>
  </article>
</section>

<!-- About -->
<h2 class="abs section-title" style="top:230px">ABOUT THE GROUP</h2>
<div class="abs title-rule" style="top:271px"></div>
<p class="abs copy" style="top:295px;left:196px;width:700px">PVT Law Group enjoys providing proactive, business-minded, efficient legal solutions for individuals and companies that benefit from major law firm experience at reasonable rates.</p>
<div class="abs emphasis">Some areas of emphasis include</div>
<p class="abs copy" style="top:397px">Counseling individuals and companies with respect to clearing, selecting, securing, managing, commercializing, and protecting intellectual<br>property assets around the world. This includes traditional global brand management, marketing,<br>advertising, and enforcement work as well as litigation.</p>
<div class="abs dash-rule"></div>
<p class="abs copy" style="top:473px">PVT Law Group also provides general counseling services for individuals and businesses, from start-up advice to sophisticated business<br>transactions strategy, agreement negotiating, dispute resolution, and litigation.</p>
<a class="abs read-more">READ MORE
  <svg viewBox="0 0 20 20"><circle cx="10" cy="10" r="8.6" fill="none" stroke="#fff" stroke-width="1.6"/><path d="M8 5.5l4.5 4.5L8 14.5" fill="none" stroke="#fff" stroke-width="2"/></svg>
</a>

<!-- Testimonials -->
<section class="abs clients" aria-label="Client testimonials"></section>
<h2 class="abs section-title" style="top:661px">WHAT OUR CLIENTS SAY</h2>
<div class="abs title-rule" style="top:701px"></div>
<div class="abs nav-btn nav-btn--pale" style="left:5px;top:818px"><svg stroke="#fff"><use href="#chev-left"/></svg></div>
<div class="abs nav-btn nav-btn--orange" style="left:1041px;top:818px"><svg stroke="#fff"><use href="#chev-right"/></svg></div>

<blockquote class="abs quote" style="left:117px">Lorem ipsum dolor sit amet, consectetur adipisicing elit, sed do eiusmod tempor incididunt ut labore et dolore magna aliqua. Ut enim ad minim veniam, quis nostrud exercitation ullamco laboris nisi ut aliquip ex ea commodo consequat. Duis aute irure dolor in reprehenderit...
  <svg class="quote__tail" viewBox="0 0 16 9"><path d="M0 0L8 9 16 0" fill="#fff" stroke="#e2e2e2"/><path d="M1 0h14" stroke="#fff" stroke-width="2"/></svg></blockquote>
<blockquote class="abs quote" style="left:414px">Lorem ipsum dolor sit amet, consectetur adipisicing elit, sed do eiusmod tempor incididunt ut labore et dolore magna aliqua. Ut enim ad minim veniam, quis nostrud exercitation ullamco laboris nisi ut aliquip ex ea commodo consequat. Duis aute irure dolor in reprehenderit...
  <svg class="quote__tail" viewBox="0 0 16 9"><path d="M0 0L8 9 16 0" fill="#fff" stroke="#e2e2e2"/><path d="M1 0h14" stroke="#fff" stroke-width="2"/></svg></blockquote>
<blockquote class="abs quote" style="left:710px">Lorem ipsum dolor sit amet, consectetur adipisicing elit, sed do eiusmod tempor incididunt ut labore et dolore magna aliqua. Ut enim ad minim veniam, quis nostrud exercitation ullamco laboris nisi ut aliquip ex ea commodo consequat. Duis aute irure dolor in reprehenderit...
  <svg class="quote__tail" viewBox="0 0 16 9"><path d="M0 0L8 9 16 0" fill="#fff" stroke="#e2e2e2"/><path d="M1 0h14" stroke="#fff" stroke-width="2"/></svg></blockquote>

<div class="abs client" style="left:131px">
  <div class="client__avatar" role="img" aria-label="Client portrait"></div>
  <div><div class="client__name">Owen Hartley</div>
    <div class="client__rate">Reviews: <div class="stars" style="fill:var(--orange)"><svg style="width:12px;height:11px"><use href="#star"/></svg><svg style="width:12px;height:11px"><use href="#star"/></svg><svg style="width:12px;height:11px"><use href="#star"/></svg><svg style="width:12px;height:11px"><use href="#star"/></svg><svg style="width:12px;height:11px"><use href="#star"/></svg></div></div></div>
</div>
<div class="abs client" style="left:428px">
  <div class="client__avatar" role="img" aria-label="Client portrait"></div>
  <div><div class="client__name">Selma Ardent</div>
    <div class="client__rate">Reviews: <div class="stars" style="fill:var(--orange)"><svg style="width:12px;height:11px"><use href="#star"/></svg><svg style="width:12px;height:11px"><use href="#star"/></svg><svg style="width:12px;height:11px"><use href="#star"/></svg><svg style="width:12px;height:11px"><use href="#star"/></svg><svg style="width:12px;height:11px"><use href="#star"/></svg></div></div></div>
</div>
<div class="abs client" style="left:725px">
  <div class="client__avatar" role="img" aria-label="Client portrait"></div>
  <div><div class="client__name">Daniel Kreel</div>
    <div class="client__rate">Reviews: <div class="stars" style="fill:var(--orange)"><svg style="width:12px;height:11px"><use href="#star"/></svg><svg style="width:12px;height:11px"><use href="#star"/></svg><svg style="width:12px;height:11px"><use href="#star"/></svg><svg style="width:12px;height:11px"><use href="#star"/></svg><svg style="width:12px;height:11px"><use href="#star"/></svg></div></div></div>
</div>

<!-- Partners -->
<section class="abs partners" aria-label="Selected clients"></section>
<div class="abs partner" style="left:172px">Norvale</div>
<div class="abs partner" style="left:370px">Brightwater Capital</div>
<div class="abs partner" style="left:542px"><i></i>Quill</div>
<div class="abs partner" style="left:690px">Corvane</div>
<div class="abs partner" style="left:900px">Tripwell</div>
</body>
</html>
```